Mend the Rift! Postcard Design for a New Book for Couples

I'm looking to create a large (5x8) 2-sided postcard to advertise my new book, Mend the Rift! A Sketched Handbook for Partners
(www.mendtherift-example.com)

- I would like it to be graphically simple but also capture the vibe of the book which is: sophisticated advice for couples presented in a lighthearted way.

Here's what should definitely be on the postcard/MUST HAVE:

- A picture of the book
- At least 2 drawings from the book: choose from what you see on the website, in the book, on the back of the book cover, in the onesheet flyer or twitter campaign (see attached onesheet flyer and twitter pics, and book cover)
- The blurb from Marisol Quenby (see attached)
- about how to reach my agent for speaking engagements (see attached)
- Website information for Mend the Rift! (www.mendtherift-example.com)
- Photo of author (download from filebox-example.net/share/7QxR2mLp9vWd4KzN/view), short bio, and mention of illustrator (see bio in document called "To include in Printorra…"

Here's what would also be good to have on the postcard if it can be done creatively and graphically appealingly/NICE TO HAVE:

- Use of the handwritten font that the book title is drawn in
-Additional drawings from the book, website or book cover
-Other blurbs (in order of importance as in the attached document)

Please improve on what my publisher created: See the attached onesheet flyer they made. I feel it is a little boxy, too packed with information, mixed fonts, etc. I'm looking for the postcard to have a cleaner and livelier vibe to it - it should communicate lightheartedness but still get across that this is a serious book.

```html
<!DOCTYPE html>
<html lang="en">
<head>
<meta charset="utf-8">
<title>Mend the Rift! – Postcard</title>
<link rel="stylesheet" href="https://fonts.googleapis.com/css2?family=Amatic+SC:wght@400;700&display=swap">
<style>
  :root {
    --sun: #fde53c;
    --cream: #fcf9cf;
    --ink: #1d1d1b;
    --red: #d9412b;
    --paper: #ffffff;
    --panel-fill: #eeeeea;
    --book-light: #fbe34a;
    --book-dark: #e9c927;
    --portrait-light: #e8dcc4;
    --portrait-dark: #b9a584;
  }
  * { margin: 0; padding: 0; box-sizing: border-box; }
  html, body { width: 1200px; height: 778px; overflow: hidden; }
  body {
    background: var(--cream);
    color: var(--ink);
    font-family: "Amatic SC", cursive;
  }
  .postcard { position: relative; width: 1200px; height: 778px; background: var(--cream); }

  /* Masthead */
  .masthead {
    position: absolute; left: 0; top: 0; width: 1200px; height: 317px;
    background: var(--sun); text-align: center;
  }
  .title {
    position: absolute; left: 0; width: 1200px; top: -8px;
    font-size: 160px; font-weight: 700; letter-spacing: 20px; line-height: 1;
    text-indent: 20px;
  }
  .subtitle {
    position: absolute; left: 0; width: 1200px; top: 150px;
    font-size: 58px; font-weight: 700; letter-spacing: 3px; line-height: 1;
  }
  .swash { position: absolute; left: 215px; top: 222px; width: 780px; height: 24px; }
  .promise {
    position: absolute; left: 0; width: 1200px; top: 250px;
    font-size: 26px; font-weight: 700; line-height: 32px; letter-spacing: 1px;
  }
  .promise .accent { color: var(--red); margin-left: 14px; }

  /* Book and sketches */
  .book-cover {
    position: absolute; left: 24px; top: 350px; width: 172px; height: 376px;
  }
  .sketch-panel {
    position: absolute; left: 220px; width: 172px;
    background: var(--paper); border: 2px solid var(--ink);
  }
  .sketch-panel.money { top: 333px; height: 204px; }
  .sketch-panel.intimacy { top: 555px; height: 204px; }
  .sketch-label {
    display: block; padding: 4px 8px 0; font-size: 27px; font-weight: 700;
    color: var(--red); line-height: 30px;
  }
  .sketch-art { display: block; margin: 4px 8px 0; width: 152px; height: 158px; }

  /* Praise */
  .blurb {
    position: absolute; left: 420px; width: 760px; text-align: center;
    font-size: 25px; font-weight: 700; line-height: 24px; letter-spacing: 0.6px;
  }
  .blurb cite { font-style: normal; color: var(--red); }
  .blurb.lead { top: 336px; }
  .blurb.second { top: 494px; }

  /* Author */
  .author {
    position: absolute; left: 430px; top: 590px; width: 750px; height: 100px;
  }
  .author-portrait { position: absolute; left: 0; top: 0; width: 96px; height: 96px; }
  .author-bio {
    position: absolute; left: 118px; top: 2px; width: 630px;
    font-size: 22px; font-weight: 700; line-height: 23px; letter-spacing: 0.4px;
  }
  .author-bio strong { color: var(--red); }

  /* Contact */
  .contact {
    position: absolute; left: 420px; top: 702px; width: 760px; text-align: center;
  }
  .website {
    display: block; font-size: 36px; font-weight: 700; line-height: 38px;
    color: var(--red); letter-spacing: 1.5px;
  }
  .agent {
    display: block; font-size: 20px; font-weight: 700; line-height: 26px; letter-spacing: 0.5px;
  }
</style>
</head>
<body>
<main class="postcard">
  <header class="masthead">
    <h1 class="title">MEND THE RIFT!</h1>
    <p class="subtitle">A SKETCHED HANDBOOK FOR PARTNERS</p>
    <svg class="swash" viewBox="0 0 780 24" aria-hidden="true">
      <path d="M4 12 C200 6 520 4 776 9" stroke="var(--red)" stroke-width="5" fill="none" stroke-linecap="round"/>
      <path d="M30 18 C260 13 500 12 700 15" stroke="var(--red)" stroke-width="3" fill="none" stroke-linecap="round"/>
    </svg>
    <p class="promise">HOW TO BREAK FREE FROM <span class="accent">THE 12 MOST COMMON ARGUMENTS</span><br>AND BUILD A RELATIONSHIP THAT LASTS</p>
  </header>

  <svg class="book-cover" viewBox="0 0 172 376" role="img" aria-label="Book cover of Mend the Rift! A Sketched Handbook for Partners, yellow with a broken heart">
    <defs>
      <linearGradient id="coverTone" x1="0" x2="1">
        <stop offset="0" stop-color="var(--book-light)"/>
        <stop offset="1" stop-color="var(--book-dark)"/>
      </linearGradient>
    </defs>
    <rect x="0" y="0" width="172" height="376" fill="url(#coverTone)"/>
  </svg>

  <figure class="sketch-panel money">
    <figcaption class="sketch-label">THE MONEY FIGHT</figcaption>
    <svg class="sketch-art" viewBox="0 0 152 158" role="img" aria-label="Sketch of a couple arguing about spending, with speech bubbles">
      <rect width="152" height="158" fill="var(--panel-fill)"/>
    </svg>
  </figure>

  <figure class="sketch-panel intimacy">
    <figcaption class="sketch-label">THE SEX FIGHT</figcaption>
    <svg class="sketch-art" viewBox="0 0 152 158" role="img" aria-label="Sketch of a couple in bed disagreeing, with speech bubbles">
      <rect width="152" height="158" fill="var(--panel-fill)"/>
    </svg>
  </figure>

  <blockquote class="blurb lead">
    <p>"MEND THE RIFT! DIGS INTO THE DYNAMICS OF UNHAPPY MARRIAGES AND EMERGES<br>
    WITH GUIDELINES THAT ARE CLEAR AND INSTANTLY APPLICABLE. ALL THIS WITH<br>
    CHARMING ILLUSTRATIONS. WHAT A GIFT TO COUPLES EVERYWHERE WHO STRUGGLE TO<br>
    LIVE LESS ANNOYINGLY EVER AFTER!"</p>
    <cite>MARISOL QUENBY, CO-AUTHOR OF THE INTERNATIONAL BESTSELLER,<br>
    HOW TO LISTEN SO HEARTS WILL OPEN</cite>
  </blockquote>

  <blockquote class="blurb second">
    <p>"I COULDN'T PUT THIS BOOK DOWN! IT'S INSIGHTFUL, INCISIVE, HILARIOUS,<br>
    AND HARD-HITTING ALL AT THE SAME TIME—NOT TO MENTION INCREDIBLY HELPFUL."</p>
    <cite>—DELPHINE ARKWRIGHT, HARROW LAW SCHOOL PROFESSOR, AUTHOR OF THE COPPER LANTERN YEARS</cite>
  </blockquote>

  <section class="author">
    <svg class="author-portrait" viewBox="0 0 96 96" role="img" aria-label="Portrait photo of the author, Dr. Lena Ashcombe">
      <defs>
        <radialGradient id="portraitTone">
          <stop offset="0" stop-color="var(--portrait-light)"/>
          <stop offset="1" stop-color="var(--portrait-dark)"/>
        </radialGradient>
      </defs>
      <circle cx="48" cy="48" r="46" fill="url(#portraitTone)" stroke="var(--ink)" stroke-width="2"/>
    </svg>
    <p class="author-bio"><strong>DR. LENA ASHCOMBE</strong> IS A CLINICAL PSYCHOLOGIST WHO HAS SPENT OVER TWENTY YEARS<br>
    HELPING COUPLES TURN THE SAME OLD FIGHT INTO A REAL CONVERSATION.<br>
    SHE SPEAKS AND TEACHES WIDELY ON LOVE, CONFLICT AND REPAIR.<br>
    ILLUSTRATIONS BY <strong>OTTO PELLWING</strong>.</p>
  </section>

  <footer class="contact">
    <span class="website">WWW.MENDTHERIFT-EXAMPLE.COM</span>
    <span class="agent">SPEAKING ENGAGEMENTS: JUNE HALVERSON, BRIGHTWELL SPEAKERS · 555-014-2290 · BOOKINGS@BRIGHTWELL-EXAMPLE.COM</span>
  </footer>
</main>
</body>
</html>
```